Wine Labels for new product to attract Millenial consumers

SipRoam Design Brief
1. Intro:
Marrabel Cellars is a 120 year old family owned Australian wine company renowned for producing traditional premium quality wines. This project is aimed at breaking through this perception of Marrabel to show main stream Australian retailers that we can be innovative and relevant and that we know who their millennial shoppers are and we know how to attract their attention. This needs to be achieved through the combination of innovative and clever design paired with a product that challenges conventional Australian wine philosophies and appeals to those wine drinkers seeking authentic and alternative wine experiences.
2. Feelings:
This new wine should evoke a new set of feelings in retailers that they don’t usually associate with Marrabel Cellars. Retailers should feel excited, challenged and impressed by our knowledge of the millennial demographic. The packaging should make the shopper feel surprised, curious, cool, aspirational, understood, adventurous, individual, fashionable, progressive and engaged. It also needs to evoke a sense of the occasion it should be consumed in, with food and friends in a fun environment and evoke a sense of conviviality and a desire for shared social interaction.
3. Look + Feel:
It shouldn’t look or feel like anything Marrabel Cellars is known for and has done before. It should not carry our branding or logo, this should be a standalone product range. It should feel modern, cool, clever and hip. It should feel real, authentic, artisanal and most of all it should challenge the traditional visual discourse of wine as bored, tired, stiff and conservative. The design should be respected piece of art in its own right. It should make the shopper feel like getting a few friends around for dinner and drinks.
4. Brand Position:
This product range needs to challenge the existing brand positioning of Marrabel Cellars. It should clearly target the millennial demographic and the hipster sub culture who are being lured into new alcohol categories by cool design and positioning. “Exposed to a barrage of drinks offerings, the report found that wine is in danger of losing Generation Y to other more engaging drinks categories such as beer, cider and spirits ……. With 18-25 year olds accounting for 25% of the wine drinking population, Millennials represent an important sector of the wine market, thus keeping their attention and interest should remain a priority for wine brands.” Grape Insight Review. “…. Wine is becoming increasingly cool with the influencers and trend setters of a whole new generation.” Pour Journal.
5. Needs:
2 wine labels, one white and one red, but linked by design. Should fit a 500 ml glass bottle and design should be able to carry over to some innovative packaging into small lots of 4 or 6 like beer. For the purpose of design use the name SipRoam White and SipRoam Red. Relating the wine to food and how it should be consumed is important as this needs to be seen as a lifestyle accessory to food to combat the anti-alcohol lobby and the socially acceptable practise of eating and drinking together as part of a social experience. An area for approximately 200 words of mandatory information and declarations needs to be provided.

https://www.examplepins.test/MarrabelCellars/siproam-moodboard/

Full brief in project description

Requirements
Must have
• Full brief in project description
Nice to have
Should not have

```html
<!DOCTYPE html>
<html lang="en">
<head>
<meta charset="utf-8">
<title>SipRoam White &amp; SipRoam Red — Labels</title>
<link rel="stylesheet" href="https://fonts.googleapis.com/css2?family=Quicksand:wght@400;500&family=Josefin+Sans:wght@300;400&display=swap">
<style>
  :root {
    --canvas-bg: #e8e6e2;
    --label-bg: #1d1a1b;
    --label-text: #f2efe9;
    --label-muted: #9b9794;
    --rule: #8e8a87;
    --white-art-a: #1f6f6a;
    --white-art-b: #2b8a80;
    --white-art-c: #6b5a3a;
    --red-art-a: #8a2a14;
    --red-art-b: #c2461f;
    --red-art-c: #5a2a18;
  }
  * { margin: 0; padding: 0; box-sizing: border-box; }
  html, body {
    width: 1200px; height: 1000px; overflow: hidden;
    background: var(--canvas-bg);
  }
  .canvas {
    position: relative; width: 1200px; height: 1000px;
    display: flex; justify-content: center; align-items: center; gap: 140px;
  }
  .label {
    position: relative; width: 260px; height: 826px;
    background: var(--label-bg);
    color: var(--label-text);
    font-family: "Josefin Sans", sans-serif;
    text-align: center;
  }
  .label__art {
    position: absolute; left: 16px; top: 16px; width: 228px; height: 400px;
  }
  .label--white .label__art,
  .label--white .label__strip {
    background:
      radial-gradient(ellipse at 70% 30%, var(--white-art-c) 0%, transparent 35%),
      linear-gradient(160deg, var(--white-art-a), var(--white-art-b) 50%, var(--white-art-a));
  }
  .label--red .label__art,
  .label--red .label__strip {
    background:
      radial-gradient(ellipse at 40% 60%, var(--red-art-b) 0%, transparent 45%),
      linear-gradient(160deg, var(--red-art-c), var(--red-art-a) 45%, var(--red-art-b));
  }
  .label__name {
    position: absolute; left: 24px; bottom: 22px;
    writing-mode: vertical-rl; transform: rotate(180deg);
    font-family: "Quicksand", sans-serif; font-weight: 400;
    font-size: 44px; letter-spacing: 2px; line-height: 1;
    color: var(--label-text);
  }
  .label__rule {
    position: absolute; left: 20px; width: 220px; height: 2px;
    background: var(--rule);
  }
  .label__rule--top { top: 444px; }
  .label__rule--bottom { top: 522px; }
  .label__vintage {
    position: absolute; left: 0; right: 0; top: 466px;
    font-size: 30px; font-weight: 300; color: var(--label-muted);
    letter-spacing: 1px;
  }
  .label__variety {
    position: absolute; left: 0; right: 0; top: 560px;
    font-size: 24px; font-weight: 400; letter-spacing: 1px;
  }
  .label__volume {
    position: absolute; left: 0; right: 0; top: 606px;
    font-size: 24px; font-weight: 400;
  }
  .label__abv {
    position: absolute; left: 0; right: 0; top: 694px;
    font-size: 20px; font-weight: 300; color: var(--label-muted);
  }
  .label__strip {
    position: absolute; left: 16px; width: 228px; top: 754px; height: 40px;
  }
</style>
</head>
<body>
  <main class="canvas">
    <article class="label label--white">
      <div class="label__art" role="img" aria-label="Abstract teal and ochre brushed canvas artwork">
        <span class="label__name">SipRoam</span>
      </div>
      <div class="label__rule label__rule--top"></div>
      <p class="label__vintage">2009</p>
      <div class="label__rule label__rule--bottom"></div>
      <p class="label__variety">White Wine</p>
      <p class="label__volume">500ML</p>
      <p class="label__abv">11%Alcohol</p>
      <div class="label__strip" role="img" aria-label="Strip of teal brushed canvas artwork"></div>
    </article>

    <article class="label label--red">
      <div class="label__art" role="img" aria-label="Abstract red and rust brushed canvas artwork">
        <span class="label__name">SipRoam</span>
      </div>
      <div class="label__rule label__rule--top"></div>
      <p class="label__vintage">2009</p>
      <div class="label__rule label__rule--bottom"></div>
      <p class="label__variety">Red Wine</p>
      <p class="label__volume">500ML</p>
      <p class="label__abv">11%Alcohol</p>
      <div class="label__strip" role="img" aria-label="Strip of red brushed canvas artwork"></div>
    </article>
  </main>
</body>
</html>
```